Brivolt VoIP COMMERCIAL PHONE FLYER

We are a full service telecom VoIP company that offers local, long distance calling plans to business clients. We offer local installations, and local service we have a hands on approach and will match or beat any competitor. We work with all types of business. We are fully HIPPA complient in the medical field

Target Market(s)

SMALL TO MEDIUM BUSINESS, Medical, Real Estate, Lawyer, Accounting

Industry/Entity Type

VoIP

Font styles to use
Serif

Colors
0054AA
0677BA
7BADD7
CADEEF
E8F1F8

Requirements
Must have
• Modern/ Current picture of phone reader friendly
Nice to have
• free flow, friendly, modern
Should not have
• stuffy, corporate feel

```html
<!DOCTYPE html>
<html lang="en">
<head>
<meta charset="utf-8">
<title>Brivolt VoIP Business Phone Flyer</title>
<link rel="stylesheet" href="https://fonts.googleapis.com/css2?family=Bebas+Neue&family=Montserrat:wght@600;700;800;900&display=swap">
<style>
  :root {
    --stage: #ededed;
    --navy: #101c58;
    --navy-deep: #0b1650;
    --red: #e8333a;
    --paper: #f3f4f6;
    --sky: #8ec6ef;
    --azure: #2f7fc1;
    --ink: #333a45;
    --white: #ffffff;
    --logo-blue: #5fb3e6;
    --device-dark: #2b2e34;
    --device-mid: #4a4f58;
  }
  * { box-sizing: border-box; margin: 0; padding: 0; }
  html, body { width: 1200px; height: 1000px; overflow: hidden; background: var(--stage); }
  .flyer {
    position: absolute; left: 302px; top: 79px; width: 596px; height: 842px;
    overflow: hidden; box-shadow: 0 2px 10px rgba(0,0,0,.25);
    font-family: "Montserrat", sans-serif;
  }
  .flyer-bg { position: absolute; inset: 0; }
  .abs { position: absolute; }
  .display { font-family: "Bebas Neue", sans-serif; font-weight: 400; line-height: 1; }

  .tag-red { left: 32px; top: 26px; width: 226px; height: 42px; padding-top: 4px; background: var(--red); color: var(--white); font-size: 43px; text-align: center; }
  .headline { left: 32px; top: 72px; color: var(--white); font-size: 61px; line-height: .83; }

  .brand { left: 380px; top: 36px; display: flex; align-items: center; gap: 10px; color: var(--logo-blue); font-size: 44px; }
  .brand-mark { width: 22px; height: 22px; background: var(--logo-blue); }

  .savings { right: 32px; top: 163px; text-align: right; }
  .savings .lead { color: var(--ink); font-size: 25px; }
  .savings .big { color: var(--red); font-size: 58px; margin-top: 0; }
  .savings .pct { display: inline-block; margin-top: 0; width: 161px; height: 53px; background: var(--red); color: var(--white);
    font-family: "Montserrat", sans-serif; font-weight: 900; font-size: 42px; text-align: center; line-height: 53px; }
  .savings .tail { color: var(--ink); font-size: 24.5px; margin-top: 4px; line-height: 1.02; }

  .phone-visual { left: 38px; top: 206px; width: 340px; height: 292px; border-radius: 16px;
    background: linear-gradient(135deg, var(--device-mid) 0%, var(--device-dark) 55%, #1c1e22 100%);
    box-shadow: 0 10px 18px rgba(0,0,0,.25); }

  .features { left: 352px; top: 487px; list-style: none; }
  .features li { display: flex; align-items: center; gap: 16px; color: var(--white); font-weight: 700; font-size: 22px; line-height: 1.22; height: 46px; }
  .features li:first-child { height: 62px; }
  .hex { width: 40px; height: 44px; flex: none; }

  .cloud { left: 343px; top: 628px; width: 200px; height: 92px; }
  .call-pill { left: 320px; top: 714px; width: 243px; height: 34px; border-radius: 17px;
    background: linear-gradient(#b6dcf6, #6ea9d8); color: var(--white); font-size: 20px; text-align: center; line-height: 36px;
    text-shadow: 0 1px 2px rgba(16,28,88,.5); }
  .contact { left: 320px; color: var(--white); display: flex; align-items: center; gap: 18px; }
  .contact svg { width: 26px; height: 26px; flex: none; }
  .contact.phone { top: 764px; font-size: 37px; }
  .contact.web { top: 802px; font-weight: 700; font-size: 22px; }

  .specialty { left: 32px; top: 614px; }
  .specialty span { display: inline-block; background: var(--azure); color: var(--white); font-weight: 800; font-size: 12.3px;
    padding: 3px 5px; border-radius: 4px; margin-bottom: 1px; }
  .perks { left: 34px; top: 668px; list-style: none; }
  .perks li { display: flex; gap: 14px; color: var(--ink); font-weight: 700; font-size: 16.5px; line-height: 1.2; margin-bottom: 8px; }
  .perks svg { width: 18px; height: 18px; flex: none; margin-top: 2px; }
  .contract-bar { left: 31px; top: 795px; width: 249px; height: 22px; background: var(--red); color: var(--white);
    font-weight: 800; font-size: 15px; text-align: center; line-height: 22px; }
</style>
</head>
<body>
<main class="flyer">
  <svg class="flyer-bg" viewBox="0 0 596 842" aria-hidden="true">
    <defs>
      <linearGradient id="topBlue" x1="0" y1="0" x2="1" y2="0.4">
        <stop offset="0" stop-color="#1d4fd3"/>
        <stop offset="1" stop-color="#121f5c"/>
      </linearGradient>
    </defs>
    <rect width="596" height="842" fill="var(--navy)"/>
    <polygon points="0,0 596,0 596,80 0,520" fill="url(#topBlue)"/>
    <polygon points="253,221 596,51 596,410 298,550 298,842 0,842 0,600" fill="var(--paper)"/>
    <polygon points="250,210 398,118 398,150 270,232" fill="#2a7bd0"/>
    <polygon points="398,118 470,76 470,104 398,150" fill="var(--sky)"/>
    <polygon points="460,410 596,320 596,360 460,450" fill="var(--sky)"/>
    <polygon points="298,550 596,410 596,842 298,842" fill="var(--navy-deep)"/>
    <polygon points="0,270 165,190 390,300 385,520 170,600 0,660" fill="var(--red)"/>
    <polygon points="0,300 160,228 350,318 350,505 170,570 0,625" fill="var(--white)"/>
    <polygon points="0,340 155,262 310,335 310,490 170,540 0,595" fill="var(--red)"/>
  </svg>

  <div class="abs display tag-red">We put your</div>
  <h1 class="abs display headline">Business voice<br>on the cloud</h1>

  <div class="abs display brand"><span class="brand-mark"></span>Brivolt</div>

  <div class="abs display savings">
    <div class="lead">We help companies</div>
    <div class="big">Save over</div>
    <div class="pct">35%</div>
    <div class="tail">On their monthly<br>phone bills</div>
  </div>

  <div class="abs phone-visual" role="img" aria-label="Photo of a modern desk video phone with HD handset and touch screen"></div>

  <ul class="abs features">
    <li><svg class="hex" viewBox="0 0 40 44"><polygon points="20,0 40,11 40,33 20,44 0,33 0,11" fill="var(--red)"/><circle cx="20" cy="19" r="7" fill="none" stroke="#fff" stroke-width="2.5"/><rect x="16" y="27" width="8" height="4" fill="#fff"/></svg>Powerfull<br>features</li>
    <li><svg class="hex" viewBox="0 0 40 44"><polygon points="20,0 40,11 40,33 20,44 0,33 0,11" fill="var(--red)"/><rect x="11" y="13" width="18" height="14" rx="3" fill="none" stroke="#fff" stroke-width="2.5"/><polygon points="14,27 20,27 14,32" fill="#fff"/></svg>Easy to use</li>
    <li><svg class="hex" viewBox="0 0 40 44"><polygon points="20,0 40,11 40,33 20,44 0,33 0,11" fill="var(--red)"/><path d="M12 14 L28 30 M28 14 L12 30" stroke="#fff" stroke-width="3.5" stroke-linecap="round"/></svg>Easy set up</li>
  </ul>

  <svg class="abs cloud" viewBox="0 0 200 92" aria-hidden="true">
    <path d="M22 92 A22 22 0 0 1 30 50 A34 34 0 0 1 92 28 A44 44 0 0 1 168 52 A22 22 0 0 1 180 92 Z" fill="#5a9fd4"/>
    <polygon points="100,22 130,56 112,56 112,92 88,92 88,56 70,56" fill="var(--navy-deep)"/>
  </svg>
  <div class="abs display call-pill">Call today for your free phones</div>

  <div class="abs contact phone display">
    <svg viewBox="0 0 24 24"><path d="M6.6 10.8a15 15 0 0 0 6.6 6.6l2.2-2.2c.3-.3.7-.4 1-.2 1.1.4 2.3.6 3.6.6.6 0 1 .4 1 1V20c0 .6-.4 1-1 1A17 17 0 0 1 3 4c0-.6.4-1 1-1h3.5c.6 0 1 .4 1 1 0 1.3.2 2.5.6 3.6.1.3 0 .7-.2 1z" fill="var(--red)"/></svg>
    (555) 014 2290
  </div>
  <div class="abs contact web">
    <svg viewBox="0 0 24 24"><circle cx="12" cy="12" r="10" fill="var(--red)"/><path d="M2 12h20M12 2c-4 4-4 16 0 20M12 2c4 4 4 16 0 20" stroke="var(--navy-deep)" stroke-width="1.6" fill="none"/></svg>
    www.brivolt.com
  </div>

  <div class="abs specialty"><span>SPECIALIZES IN BUSINESS</span><br><span>COMMUNICATION CLOUD SOLUTIONS!</span></div>
  <ul class="abs perks">
    <li><svg viewBox="0 0 18 18"><circle cx="9" cy="9" r="7.5" fill="none" stroke="var(--red)" stroke-width="1.6"/><path d="M5 9l3 3 6-6" stroke="var(--red)" stroke-width="1.8" fill="none"/></svg>Month to month<br>plans available</li>
    <li><svg viewBox="0 0 18 18"><circle cx="9" cy="9" r="7.5" fill="none" stroke="var(--red)" stroke-width="1.6"/><path d="M5 9l3 3 6-6" stroke="var(--red)" stroke-width="1.8" fill="none"/></svg>No long term contracts</li>
    <li><svg viewBox="0 0 18 18"><circle cx="9" cy="9" r="7.5" fill="none" stroke="var(--red)" stroke-width="1.6"/><path d="M5 9l3 3 6-6" stroke="var(--red)" stroke-width="1.8" fill="none"/></svg>3 Month free service<br>offer available</li>
  </ul>
  <div class="abs contract-bar">1 YEAR CONTRACT</div>
</main>
</body>
</html>
```